New custom software business needs a Wordpress site

We need a Wordpress site for a new company based out of Chicago called 'Vellora Consulting'. Using a mix of on and off-shore resources we build custom software solutions, mainly focusing on small to medium sized companies. We help our customers "aspire" to do great things.
We have a basic site up here: https://brindlewave.example/. We worked on the content for it but not the branding. For now, this houses all the pages (except for a Contact Us page we'll be adding soon) for the foreseeable future.
We also have a new logo (attached) that we'd like to base the styling/colors on.
Target Market(s)
Small to medium sized companies that require tech resources
Industry/Entity Type
Software
Nice to have
- Teamwork, tech, professional but not elitist

```html
<!DOCTYPE html>
<html lang="en">
<head>
<meta charset="utf-8">
<title>Vellora Consulting</title>
<link href="https://fonts.googleapis.com/css2?family=Montserrat:wght@400;500;600;700&display=swap" rel="stylesheet">
<style>
:root{
  --canvas:#eef0f3;
  --blue:#0b50b0;
  --blue-title:#1b5fb5;
  --blue-soft:#7ea8d8;
  --blue-light:#6aa6e2;
  --band:#e3edf8;
  --ink:#2a2f3a;
  --muted:#8a93a2;
  --footer:#0a1322;
  --white:#ffffff;
  --line:#dfe3ea;
}
*{margin:0;padding:0;box-sizing:border-box}
html,body{width:1200px;height:3462px;overflow:hidden}
body{background:var(--canvas);font-family:"Montserrat",sans-serif;color:var(--ink)}
.page{position:absolute;left:178px;top:382px;width:844px;height:2698px;background:var(--white);box-shadow:0 4px 24px rgba(10,30,70,.12);overflow:hidden}
.abs{position:absolute}
.brand{display:flex;align-items:center;gap:8px}
.brand-mark{width:26px;height:26px;background:var(--blue)}
.brand-name{font-weight:600;font-size:19px;letter-spacing:1px;color:var(--blue-title)}
.nav{display:flex;gap:20px;font-size:9.5px;font-weight:500;color:var(--ink);white-space:nowrap}
.nav a{color:inherit;text-decoration:none}
.nav .active{color:var(--blue);text-decoration:underline;text-underline-offset:3px}
.btn{position:absolute;display:flex;align-items:center;justify-content:center;font-size:9px;font-weight:500;color:var(--white);letter-spacing:.3px;white-space:nowrap}
.btn-dark{background:var(--blue)}
.btn-soft{background:var(--blue-soft)}
.photo{position:absolute}
.hero-title{position:absolute;left:0;width:844px;text-align:center;color:var(--white);font-weight:700;font-size:32px;line-height:42px;letter-spacing:.5px}
.hero-title em{font-style:normal;color:var(--blue-light)}
.h2{position:absolute;left:0;width:844px;text-align:center;font-weight:700;font-size:21px;color:var(--blue-title);letter-spacing:.5px}
.h2::after{content:"";display:block;width:36px;height:2px;background:var(--blue-title);margin:6px auto 0}
.about-title{left:62px;top:490px;font-weight:700;font-size:20px;line-height:28px;color:var(--blue-title)}
.about-rule{left:62px;top:580px;width:62px;height:2px;background:var(--blue-title)}
.body-text{font-size:9px;line-height:13.4px;color:var(--ink)}
.svc-title{font-weight:700;font-size:15px;line-height:22px;color:var(--blue-title)}
.frame{position:absolute;border:1.5px solid var(--blue-soft)}
.leader{font-size:13.5px;color:var(--ink)}
.leader b{color:var(--blue);font-weight:700}
.dots{display:flex;gap:11px;align-items:center}
.dots span{width:7px;height:7px;border-radius:50%;background:#1d2330}
.dots span.on{width:15px;height:15px;background:var(--blue)}
.team-photo{position:absolute;width:126px;height:147px;border:1px solid #c9ced6;padding:3px;background:var(--white)}
.team-photo div{width:100%;height:100%;background:linear-gradient(160deg,#d9d5cf,#8d8175)}
.blogs{left:0;top:1645px;width:844px;height:410px;background:var(--blue)}
.blogs .h2{color:var(--white)}
.blogs .h2::after{background:var(--white)}
.blog-card{position:absolute;top:107px;width:228px}
.blog-card .img{height:128px;border:1.5px solid #8fb4e4}
.blog-card p{margin-top:14px;font-size:9px;line-height:13px;color:var(--white)}
.blog-meta{margin-top:13px;display:flex;align-items:center;gap:8px;font-size:8.5px;color:var(--white)}
.blog-meta a{color:#a9c8ef;text-decoration:underline}
.cal{width:9px;height:9px;border:1.3px solid var(--white);border-top-width:3px}
.field{position:absolute;border:1px solid var(--line);display:flex;align-items:center;gap:8px;padding-left:11px;font-size:8.5px;color:#a2aab6}
.field i{width:7px;height:7px;border:1.3px solid var(--blue-soft);border-radius:2px}
.field.tall{align-items:flex-start;padding-top:12px}
.footer{left:0;top:2420px;width:844px;height:278px;background:var(--footer)}
.contact-box{position:absolute;left:75px;top:120px;width:695px;height:57px;background:var(--white);display:flex;align-items:center;padding:0 18px;font-size:9px;color:var(--ink)}
.contact-item{display:flex;align-items:center;gap:9px}
.foot-nav{position:absolute;top:204px;left:0;width:844px;display:flex;justify-content:center;gap:22px;font-size:9px;font-weight:500;color:var(--white)}
.foot-nav .active{text-decoration:underline;text-underline-offset:3px}
.copy{position:absolute;top:232px;left:0;width:844px;text-align:center;font-size:8.5px;color:var(--white)}
</style>
</head>
<body>
<main class="page">

  <!-- Header -->
  <header>
    <div class="abs brand" style="left:62px;top:20px">
      <span class="brand-mark"></span><span class="brand-name">VELLORA</span>
    </div>
    <nav class="abs nav" style="left:306px;top:28px">
      <a class="active">HOME</a>
      <a>ABOUT US</a>
      <a>SERVICES</a>
      <a>TEAM</a>
      <a>BLOG</a>
      <a>CONTACT US</a>
    </nav>
    <div class="btn btn-dark" style="left:680px;top:21px;width:102px;height:25px">CONSULT NOW!</div>
  </header>

  <!-- Hero -->
  <section>
    <div class="photo" role="img" aria-label="Business team shaking hands across a meeting table" style="left:0;top:68px;width:844px;height:354px;background:linear-gradient(120deg,#5c5750 0%,#7d7469 35%,#4b5360 65%,#2f3a4a 100%)"></div>
    <div class="abs" style="left:0;top:68px;width:844px;height:354px;background:rgba(10,20,40,.32)"></div>
    <h1 class="hero-title" style="top:183px">WE HELP OUR<br>CUSTOMERS "<em>ASPIRE</em>" TO<br>DO GREAT THINGS.</h1>
  </section>

  <!-- About -->
  <section>
    <h2 class="abs about-title">WE ARE A YOUNG<br>MANAGEMENT SOFTWARE<br>CONSULTING FIRM.</h2>
    <div class="abs about-rule"></div>
    <div class="abs body-text" style="left:429px;top:485px;width:354px">
      <p>Welcome to Vellora, a software consulting company specializing in serving small to medium size businesses. We understand the unique challenges and opportunities that these companies face, and we are dedicated to helping them succeed through innovative technology solutions.</p>
      <p style="margin-top:13px">Our team of experienced professionals has a diverse range of skills and expertise, making us well-equipped to handle any project, big or small. We specialize in custom software development, working closely with our clients to understand their specific needs and build solutions that meet their requirements.</p>
    </div>
    <div class="btn btn-soft" style="left:429px;top:641px;width:83px;height:24px">ABOUT US</div>
  </section>

  <!-- Services -->
  <section>
    <h2 class="h2" style="top:727px">SERVICES</h2>
    <div class="abs" style="left:0;top:818px;width:844px;height:455px;background:var(--band)"></div>

    <div class="frame" style="left:67px;top:783px;width:331px;height:256px"></div>
    <div class="photo" role="img" aria-label="Laptop with glowing document and security icons floating above the keyboard" style="left:62px;top:788px;width:330px;height:251px;background:linear-gradient(135deg,#5a4a40,#2f2d33 50%,#8a6a52)"></div>
    <div class="abs svc-title" style="left:453px;top:852px">CUSTOM<br>SOLUTION DELIVERY</div>
    <p class="abs body-text" style="left:453px;top:899px;width:260px">Vellora offers a range of services focused on helping businesses and organizations deliver software solutions to their customers or users.</p>
    <div class="btn btn-dark" style="left:453px;top:955px;width:92px;height:24px">READ MORE</div>

    <div class="frame" style="left:446px;top:1048px;width:331px;height:256px"></div>
    <div class="photo" role="img" aria-label="Businessman touching a network of connected people icons" style="left:452px;top:1052px;width:330px;height:251px;background:linear-gradient(135deg,#3c4658,#6b7a92 55%,#c9cfdc)"></div>
    <div class="abs svc-title" style="left:62px;top:1106px;width:330px;text-align:right">STAFF<br>AUGMENTATION</div>
    <p class="abs body-text" style="left:112px;top:1152px;width:280px;text-align:right">Let Vellora help you supplement your existing software development teams with additional resources and expertise. We provided access to experienced</p>
    <div class="btn btn-soft" style="left:300px;top:1205px;width:92px;height:24px">READ MORE</div>
  </section>

  <!-- Team -->
  <section>
    <h2 class="h2" style="top:1369px">OUR TEAM</h2>

    <div class="team-photo" style="left:62px;top:1430px"><div role="img" aria-label="Portrait of team leader Dario"></div></div>
    <div class="abs leader" style="left:205px;top:1441px">As a leader, <b>Dario</b></div>
    <div class="abs dots" style="left:210px;top:1469px"><span></span><span></span><span></span><span></span></div>
    <p class="abs body-text" style="left:205px;top:1490px;width:200px">is dedicated to fostering a culture of collaboration, innovation, and excellence within his team. He believes that by...</p>
    <div class="btn btn-dark" style="left:207px;top:1545px;width:84px;height:21px;font-size:8px">READ MORE</div>

    <div class="team-photo" style="left:440px;top:1430px"><div role="img" aria-label="Portrait of team leader Elliot"></div></div>
    <div class="abs leader" style="left:583px;top:1441px">As a leader, <b>Elliot</b></div>
    <div class="abs dots" style="left:588px;top:1465px"><span></span><span></span><span class="on"></span><span></span></div>
    <p class="abs body-text" style="left:583px;top:1490px;width:200px">is dedicated to fostering a culture of collaboration, innovation, and excellence within his team. He believes that by...</p>
    <div class="btn btn-soft" style="left:585px;top:1545px;width:84px;height:21px;font-size:8px">READ MORE</div>
  </section>

  <!-- Blogs -->
  <section class="abs blogs">
    <h2 class="h2" style="top:52px">BLOGS</h2>
    <article class="blog-card" style="left:62px">
      <div class="img" role="img" aria-label="Smiling businesswoman in a bright office meeting" style="background:linear-gradient(135deg,#e9e6e1,#a28a74)"></div>
      <p>Lorem Ipsum is simply dummy text of the printing and typesetting...</p>
      <div class="blog-meta"><span class="cal"></span>26 Dec, 2022 <span>|</span> <a>READ MORE</a></div>
    </article>
    <article class="blog-card" style="left:308px">
      <div class="img" role="img" aria-label="Team working with digital technology overlays" style="background:linear-gradient(135deg,#2c4c7e,#6f93c4 60%,#d2def0)"></div>
      <p>Lorem Ipsum is simply dummy text of the printing and typesetting...</p>
      <div class="blog-meta"><span class="cal"></span>26 Dec, 2022 <span>|</span> <a>READ MORE</a></div>
    </article>
    <article class="blog-card" style="left:554px">
      <div class="img" role="img" aria-label="Colleagues talking together in a modern office" style="background:linear-gradient(135deg,#dfe4ea,#7b8796 60%,#3b4250)"></div>
      <p>Lorem Ipsum is simply dummy text of the printing and typesetting...</p>
      <div class="blog-meta"><span class="cal"></span>26 Dec, 2022 <span>|</span> <a style="color:var(--white)">READ MORE</a></div>
    </article>
    <div class="btn btn-soft" style="left:382px;top:331px;width:80px;height:24px">VIEW ALL</div>
  </section>

  <!-- Quick inquiry -->
  <section>
    <h2 class="h2" style="top:2125px">QUICK INQUIRY</h2>
    <div class="field" style="left:213px;top:2170px;width:204px;height:26px"><i></i>First Name</div>
    <div class="field" style="left:428px;top:2170px;width:204px;height:26px"><i></i>Last Name</div>
    <div class="field" style="left:213px;top:2206px;width:204px;height:26px"><i></i>Email</div>
    <div class="field" style="left:428px;top:2206px;width:204px;height:26px"><i></i>Phone</div>
    <div class="field tall" style="left:213px;top:2243px;width:419px;height:68px"><i></i>How can we help?</div>
    <div class="btn btn-soft" style="left:384px;top:2334px;width:76px;height:23px">SUBMIT</div>
  </section>

  <!-- Footer -->
  <footer class="abs footer">
    <div class="abs brand" style="left:322px;top:52px">
      <span class="brand-mark" style="width:34px;height:34px;background:var(--blue-light)"></span>
      <span class="brand-name" style="color:var(--white);font-size:22px">VELLORA</span>
    </div>
    <div class="contact-box">
      <div class="contact-item" style="width:190px">
        <svg width="11" height="14" viewBox="0 0 11 14"><path d="M5.5 0C2.5 0 0 2.4 0 5.4 0 9.4 5.5 14 5.5 14S11 9.4 11 5.4C11 2.4 8.5 0 5.5 0z" fill="#0b50b0"/><circle cx="5.5" cy="5.3" r="2" fill="#fff"/></svg>
        <span style="line-height:12px">1418 W. Larkspur Avenue, Suite<br>420, Chicago IL 60610</span>
      </div>
      <div class="contact-item" style="width:184px">
        <svg width="14" height="10" viewBox="0 0 14 10"><rect width="14" height="10" fill="#0b50b0"/><path d="M0 0l7 5.5L14 0" stroke="#fff" fill="none" stroke-width="1.2"/></svg>
        info@velloracon.example
      </div>
      <div class="contact-item" style="width:170px">
        <svg width="12" height="12" viewBox="0 0 12 12"><path d="M2.4 0.5l2 2.4-1.2 1.6c.9 1.8 2.3 3.2 4.2 4.2l1.6-1.2 2.4 2-1.2 2C5.1 11.2 0.8 6.9 0.5 1.7z" fill="#0b50b0"/></svg>
        312-555-0148
      </div>
      <div class="dots" style="margin-left:auto"><span></span><span></span><span class="on"></span><span></span></div>
    </div>
    <nav class="foot-nav">
      <span class="active">HOME</span><span>ABOUT US</span><span>SERVICES</span><span>TEAM</span><span>BLOG</span><span>CONTACT US</span>
    </nav>
    <p class="copy">Copyright © 2022 Vellora Consulting. All Rights Reserved</p>
    <svg class="abs" style="left:722px;top:223px" width="24" height="24" viewBox="0 0 24 24"><circle cx="12" cy="12" r="11" fill="none" stroke="#5c6576" stroke-width="1.2"/><path d="M8 13l4-4 4 4M12 9v8M8 7h8" stroke="#5c6576" stroke-width="1.2" fill="none"/></svg>
  </footer>

</main>
</body>
</html>
```